Custom Cakes- Nonprofit Organization Stationery Set

We are looking for a FULL set stationery design for our organization.
We create custom cakes for children in foster care and work with teens and young adults who have intellectual and developmental disabilities.
We spare no expense or amount of time creating fantastic cakes for these kids.... therefore are marketing materials need to reflect the same amount of fine details.

* Business Card Design (Front/Back preferred)
* Letterhead
* Envelope
* Presentation Folder

**** Tagline: Fostering Amazing Memories
would like this to appear on business card and marketing materials

Marlene Pruitt - Founder/Executive Director
www.brightcrumb.org
info@brightcrumb.org
1-855-MY-CRUMBS
1-855-692-7862

Address is optional
PO Box 7264
Alpharetta, GA 30187

• Contact Information
• PO Box Address, design that will go well with textured/colored business card paper
• Updated: Business cards (maybe) textured paper, foiled, embossed or colored edges

```html
<!DOCTYPE html>
<html lang="en">
<head>
<meta charset="utf-8">
<title>Bright Crumb Foundation – Presentation Folder</title>
<link href="https://fonts.googleapis.com/css2?family=Didact+Gothic&display=swap" rel="stylesheet">
<style>
  :root {
    --backdrop: #e6e6e6;
    --paper: #ffffff;
    --fold-shade: #ececec;
    --ink: #1a1a1a;
    --accent-pink: #e6157f;
    --soft-shadow: rgba(0, 0, 0, 0.18);
  }
  * { margin: 0; padding: 0; box-sizing: border-box; }
  html, body {
    width: 1200px;
    height: 1000px;
    overflow: hidden;
    background: var(--backdrop);
    font-family: "Didact Gothic", "Century Gothic", sans-serif;
    color: var(--ink);
  }
  .folder-spread {
    position: absolute;
    left: 150px;
    top: 200px;
    width: 900px;
    height: 600px;
    display: flex;
    box-shadow: 0 12px 30px var(--soft-shadow);
  }
  .folder-panel {
    position: relative;
    width: 450px;
    height: 600px;
    background: var(--paper);
  }
  .folder-panel--back {
    background: linear-gradient(to right, var(--paper) 80%, var(--fold-shade) 100%);
  }
  .folder-panel--front {
    background: linear-gradient(to right, var(--fold-shade) 0%, var(--paper) 12%);
  }
  .brand-block {
    display: flex;
    flex-direction: column;
    align-items: center;
    text-align: center;
  }
  .brand-block__mark {
    display: block;
    border-radius: 50%;
    background: var(--accent-pink);
  }
  .brand-block__name {
    color: var(--ink);
    font-weight: 400;
    line-height: 1.05;
  }
  .brand-block__tagline {
    color: var(--accent-pink);
    font-weight: 400;
    letter-spacing: 0.08em;
  }
  .folder-panel--front .brand-block {
    position: absolute;
    left: 0;
    right: 0;
    top: 110px;
    gap: 18px;
  }
  .folder-panel--front .brand-block__mark { width: 96px; height: 96px; }
  .folder-panel--front .brand-block__name { font-size: 46px; }
  .folder-panel--front .brand-block__tagline { font-size: 19px; }
  .folder-panel--back .brand-block {
    position: absolute;
    left: 25px;
    bottom: 38px;
    width: 170px;
    gap: 8px;
  }
  .folder-panel--back .brand-block__mark { width: 42px; height: 42px; }
  .folder-panel--back .brand-block__name { font-size: 19px; }
  .folder-panel--back .brand-block__tagline { font-size: 10px; letter-spacing: 0.04em; }
  .contact-list {
    position: absolute;
    left: 250px;
    bottom: 50px;
    list-style: none;
    font-size: 15px;
    line-height: 1.25;
  }
  .contact-list__item {
    display: flex;
    align-items: flex-start;
    gap: 10px;
    margin-bottom: 4px;
  }
  .contact-list__icon {
    width: 17px;
    height: 17px;
    flex: none;
    margin-top: 1px;
    fill: var(--accent-pink);
  }
</style>
</head>
<body>
  <main class="folder-spread">
    <section class="folder-panel folder-panel--back">
      <div class="brand-block">
        <span class="brand-block__mark"></span>
        <span class="brand-block__name">Bright Crumb<br>Foundation</span>
        <span class="brand-block__tagline">Fostering Amazing Memories</span>
      </div>
      <ul class="contact-list">
        <li class="contact-list__item">
          <svg class="contact-list__icon" viewBox="0 0 16 16" aria-hidden="true"><circle cx="8" cy="8" r="7.5"/><path d="M1 8h14M8 1c-3 3-3 11 0 14M8 1c3 3 3 11 0 14" stroke="#fff" stroke-width="1.2" fill="none"/></svg>
          <span>www.brightcrumb.org</span>
        </li>
        <li class="contact-list__item">
          <svg class="contact-list__icon" viewBox="0 0 16 16" aria-hidden="true"><rect x="0.5" y="3" width="15" height="10" rx="1"/><path d="M1 4l7 5 7-5" stroke="#fff" stroke-width="1.2" fill="none"/></svg>
          <span>info@brightcrumb.org</span>
        </li>
        <li class="contact-list__item">
          <svg class="contact-list__icon" viewBox="0 0 16 16" aria-hidden="true"><path d="M3 1h3l1.5 4-2 1.3a9 9 0 0 0 4.2 4.2l1.3-2 4 1.5v3a1 1 0 0 1-1 1A14 14 0 0 1 2 2a1 1 0 0 1 1-1z"/></svg>
          <span>1-855-MY-CRUMBS</span>
        </li>
        <li class="contact-list__item">
          <svg class="contact-list__icon" viewBox="0 0 16 16" aria-hidden="true"><path d="M3 1h3l1.5 4-2 1.3a9 9 0 0 0 4.2 4.2l1.3-2 4 1.5v3a1 1 0 0 1-1 1A14 14 0 0 1 2 2a1 1 0 0 1 1-1z"/></svg>
          <span>1-855-692-7862</span>
        </li>
        <li class="contact-list__item">
          <svg class="contact-list__icon" viewBox="0 0 16 16" aria-hidden="true"><path d="M8 0a5.5 5.5 0 0 0-5.5 5.5C2.5 10 8 16 8 16s5.5-6 5.5-10.5A5.5 5.5 0 0 0 8 0z"/><circle cx="8" cy="5.5" r="2" fill="#fff"/></svg>
          <span>PO Box 7264<br>Alpharetta, GA 30187</span>
        </li>
      </ul>
    </section>
    <section class="folder-panel folder-panel--front">
      <div class="brand-block">
        <span class="brand-block__mark"></span>
        <span class="brand-block__name">Bright Crumb<br>Foundation</span>
        <span class="brand-block__tagline">Fostering Amazing Memories</span>
      </div>
    </section>
  </main>
</body>
</html>
```